Packaging for coffee beans bag

looking for design for bags packaging for our coffee beans brand (logo attached) with special green color (you can select the best green color grade) for the sizes 1KG and 500GRAMS.
attached also pictures for our old packaging what we are looking to change.
attached the ai file for the final project.

```html
<!DOCTYPE html>
<html lang="en">
<head>
<meta charset="utf-8">
<title>Sahra Roast – Coffee Bag Dieline</title>
<link rel="stylesheet" href="https://fonts.googleapis.com/css2?family=Montserrat:wght@400;600;800&display=swap">
<style>
  :root{
    --bag-green:#1e9a5c;
    --bag-green-deep:#16804b;
    --bag-green-light:#2fb06e;
    --gold:#d8a51e;
    --ink-white:#ffffff;
    --dim-blue:#5b86b8;
    --page:#ffffff;
  }
  *{margin:0;padding:0;box-sizing:border-box}
  html,body{width:900px;height:1200px;overflow:hidden;background:var(--page)}
  body{font-family:'Montserrat',Arial,sans-serif;position:relative}
  .dieline{position:absolute;left:0;top:0;width:900px;height:1200px}
  .dim-text{font-family:'Montserrat',Arial,sans-serif;font-size:15px;fill:var(--dim-blue);font-weight:600}
  .dim-line{stroke:var(--dim-blue);stroke-width:1.2}
  .brand{font-family:'Montserrat',Arial,sans-serif;font-weight:800;fill:var(--gold);letter-spacing:2px}
  .info{font-family:'Montserrat',Arial,sans-serif;font-size:9px;fill:var(--ink-white)}
  .form-label{font-family:'Montserrat',Arial,sans-serif;font-size:10px;fill:var(--ink-white)}
  .legend{position:absolute;left:560px;top:905px;display:flex;gap:34px;font-size:18px;align-items:center}
  .legend-item{display:flex;align-items:center;gap:10px}
  .swatch{width:30px;height:30px;display:block}
  .swatch--gold{background:var(--gold)}
  .swatch--green{background:var(--bag-green)}
</style>
</head>
<body>
<svg class="dieline" viewBox="0 0 900 1200" xmlns="http://www.w3.org/2000/svg">
  <defs>
    <linearGradient id="leafTone" x1="0" y1="0" x2="1" y2="1">
      <stop offset="0" stop-color="var(--bag-green-light)"/>
      <stop offset="1" stop-color="var(--bag-green)"/>
    </linearGradient>
  </defs>

  <!-- dimensions -->
  <g class="dimensions">
    <line class="dim-line" x1="66" y1="58" x2="834" y2="58"/>
    <line class="dim-line" x1="66" y1="50" x2="66" y2="66"/>
    <line class="dim-line" x1="834" y1="50" x2="834" y2="66"/>
    <text class="dim-text" x="450" y="48" text-anchor="middle">384 mm</text>
    <text class="dim-text" x="22" y="124" font-size="11">30mm</text>
    <line class="dim-line" x1="48" y1="150" x2="48" y2="730"/>
    <text class="dim-text" x="40" y="440" transform="rotate(-90 40 440)" text-anchor="middle">290 mm</text>
    <line class="dim-line" x1="852" y1="150" x2="852" y2="730"/>
    <text class="dim-text" x="868" y="300" transform="rotate(-90 868 300)" text-anchor="middle">225</text>
    <text class="dim-text" x="868" y="650" transform="rotate(-90 868 650)" text-anchor="middle">65</text>
    <line class="dim-line" x1="66" y1="885" x2="834" y2="885"/>
    <text class="dim-text" x="131" y="878" text-anchor="middle">65</text>
    <text class="dim-text" x="323" y="878" text-anchor="middle">127</text>
    <text class="dim-text" x="515" y="878" text-anchor="middle">65</text>
    <text class="dim-text" x="707" y="878" text-anchor="middle">127</text>
  </g>

  <!-- bag body with leaf pattern tone -->
  <rect x="66" y="90" width="768" height="640" rx="10" fill="url(#leafTone)" role="img" aria-label="Scattered outline coffee leaves pattern over green"/>
  <!-- bottom gusset tab -->
  <rect x="196" y="730" width="254" height="130" rx="10" fill="var(--bag-green)"/>
  <!-- side notches -->
  <path d="M66 690 L196 690 L196 730 L66 730 Z M450 690 L580 690 L580 730 L450 730 Z" fill="var(--bag-green-deep)"/>

  <!-- fold lines -->
  <g stroke="var(--ink-white)" stroke-opacity=".35" stroke-dasharray="4 4">
    <line x1="66" y1="150" x2="834" y2="150"/>
    <line x1="196" y1="90" x2="196" y2="730"/>
    <line x1="450" y1="90" x2="450" y2="730"/>
    <line x1="580" y1="90" x2="580" y2="730"/>
    <line x1="196" y1="730" x2="450" y2="730"/>
  </g>

  <!-- front panel -->
  <g class="front-panel">
    <text class="info" x="323" y="178" text-anchor="middle">ARABICA</text>
    <rect x="236" y="188" width="174" height="120" rx="14" fill="none" stroke="var(--ink-white)" stroke-width="2"/>
    <circle cx="323" cy="225" r="16" fill="var(--gold)"/>
    <text class="brand" x="323" y="270" font-size="22" text-anchor="middle">SAHRA</text>
    <text class="brand" x="323" y="293" font-size="14" text-anchor="middle">ROAST</text>
  </g>

  <!-- back panel -->
  <g class="back-panel">
    <rect x="620" y="170" width="174" height="110" rx="12" fill="none" stroke="var(--ink-white)" stroke-width="2"/>
    <circle cx="707" cy="202" r="13" fill="var(--gold)"/>
    <text class="brand" x="707" y="245" font-size="19" text-anchor="middle">SAHRA</text>
    <text class="brand" x="707" y="266" font-size="12" text-anchor="middle">ROAST</text>

    <rect x="606" y="310" width="202" height="150" rx="6" fill="none" stroke="var(--ink-white)" stroke-width="1.2"/>
    <text class="info" x="707" y="326" text-anchor="middle">www.sahraroast.example</text>
    <g stroke="var(--ink-white)" stroke-opacity=".6">
      <line x1="606" y1="334" x2="808" y2="334"/>
      <line x1="606" y1="355" x2="808" y2="355"/>
      <line x1="606" y1="376" x2="808" y2="376"/>
      <line x1="606" y1="397" x2="808" y2="397"/>
      <line x1="606" y1="418" x2="808" y2="418"/>
      <line x1="606" y1="439" x2="808" y2="439"/>
      <line x1="690" y1="334" x2="690" y2="460"/>
    </g>
    <text class="info" x="612" y="348">Origin</text><text class="info" x="696" y="348">Ethiopia</text>
    <text class="info" x="612" y="369">Altitude</text><text class="info" x="696" y="369">1900 m</text>
    <text class="info" x="612" y="390">Process</text><text class="info" x="696" y="390">Washed</text>
    <text class="info" x="612" y="411">Roast</text><text class="info" x="696" y="411">Medium</text>
    <text class="info" x="612" y="432">Notes</text><text class="info" x="696" y="432">Citrus, cocoa</text>
    <text class="info" x="612" y="453">Grind</text><text class="info" x="696" y="453">Whole bean</text>
    <text class="info" x="707" y="480" text-anchor="middle">Net weight 500g</text>
  </g>

  <!-- bottom tab form -->
  <g class="batch-form">
    <rect x="236" y="752" width="174" height="86" rx="6" fill="none" stroke="var(--ink-white)" stroke-width="1.2"/>
    <text class="form-label" x="246" y="776">Roast date</text>
    <rect x="320" y="766" width="80" height="14" fill="var(--ink-white)"/>
    <text class="form-label" x="246" y="801">Exp. date</text>
    <rect x="320" y="791" width="80" height="14" fill="var(--ink-white)"/>
    <text class="form-label" x="246" y="826">Batch no.</text>
    <rect x="320" y="816" width="80" height="14" fill="var(--ink-white)"/>
  </g>
</svg>

<div class="legend">
  <div class="legend-item"><span class="swatch swatch--gold"></span>Gold</div>
  <div class="legend-item"><span class="swatch swatch--green"></span>Green</div>
</div>
</body>
</html>
```